Legislative compliance to home owners, landlords and agents

Logo, business card and stationaly header for a sole trader offering sevices in the UK to home owners, landlords and Letting agents to meet legislation requirement relating to sale and leasing of rental domestic homes. Services offered include Legionella Risk Assessment, Portable Appliance Testing and Energy Performance Certificates. Logo to include depiction of a house and compliance tick list images. Have an existing card with water splash image to reflect water testing, so considering picking up same wave blue. Company name Talvane Property Services. Web www.talvaneps-example.com. email: info@talvaneps-example.com. Address: Glenmorrow, Aberdeen. All three services to be listed. Name as existing card.,

Target Market(s)

UK home owners, landlords, lettings and estate agents

Industry/Entity Type

Property Management

Contact Information for Business Card

Derek Hollingsby CEng, MSoHTF
Address: Glenmorrow, Aberdeen
Web: www.talvaneps-example.com
e-mail info@talvaneps-example.com
Phone: 07921 458 302
Services: Legionella Risk Assessment, Portable Appliance Testing, Energy Performance Certificate

Logo Text

Talvane Property Services

Font styles to use
Sans Serif

Colors

Designer to choose colors to be used in the design.

Requirements
Must have
• Suitable for standard UK business card size 85 mm x 55 mm, with allowance for safety border/ bleed such that colours extend to outside border of card once printed
Nice to have
• Clear font style and layout
• Happy to see images depicting phone, address etc

```html
<!DOCTYPE html>
<html lang="en">
<head>
<meta charset="utf-8">
<title>Talvane Property Services – Business Card</title>
<link rel="stylesheet" href="https://fonts.googleapis.com/css2?family=Open+Sans:wght@400;600&display=swap">
<style>
  :root {
    --backdrop: #000000;
    --card: #ffffff;
    --wave-blue: #1fbcef;
    --deep-blue: #0f5f86;
    --text-blue: #1cb3e6;
    --name-ink: #135f86;
  }
  * { box-sizing: border-box; margin: 0; padding: 0; }
  html, body {
    width: 1200px; height: 1011px; overflow: hidden;
    background: var(--backdrop);
    font-family: "Open Sans", Arial, sans-serif;
  }
  .card {
    position: absolute; left: 100px; top: 220px;
    width: 1000px; height: 570px;
    background: var(--card); overflow: hidden;
  }
  .card-shapes { position: absolute; inset: 0; }
  .brand {
    position: absolute; left: 40px; top: 150px; width: 410px;
    text-align: center;
  }
  .brand-dot {
    display: block; width: 150px; height: 150px; margin: 0 auto 26px;
    border-radius: 50%; background: var(--deep-blue);
  }
  .brand-name {
    font-size: 29px; font-weight: 400; color: var(--deep-blue);
    letter-spacing: 0.5px; white-space: nowrap;
  }
  .holder {
    position: absolute; left: 78px; top: 424px;
    font-size: 23px; font-weight: 600; color: var(--name-ink);
    white-space: nowrap;
  }
  .services-title {
    position: absolute; left: 538px; top: 124px;
    font-size: 42px; color: var(--text-blue);
  }
  .service-list, .contact-list { position: absolute; left: 502px; list-style: none; }
  .service-list { top: 180px; }
  .contact-list { top: 312px; }
  .service-list li, .contact-list li {
    display: flex; align-items: center; gap: 14px;
    font-size: 28px; color: var(--text-blue); white-space: nowrap;
  }
  .service-list li { height: 38.5px; }
  .contact-list li { height: 46px; }
  .contact-list li:nth-child(1) { height: 40px; }
  .icon { width: 22px; height: 22px; flex: none; }
</style>
</head>
<body>
  <div class="card">
    <svg class="card-shapes" viewBox="0 0 1000 570" aria-hidden="true">
      <defs>
        <linearGradient id="fold-shade" x1="0" y1="0" x2="1" y2="0">
          <stop offset="0" stop-color="#000" stop-opacity="0"/>
          <stop offset="1" stop-color="#000" stop-opacity="0.12"/>
        </linearGradient>
      </defs>
      <rect class="top-band" x="0" y="0" width="1000" height="20" fill="var(--deep-blue)"/>
      <polygon class="corner-fold-shadow" points="768,0 1000,262 1000,274 756,0" fill="url(#fold-shade)"/>
      <polygon class="corner-top-right" points="781,0 1000,0 1000,262" fill="var(--wave-blue)"/>
      <polygon class="corner-bottom-left" points="0,374 0,570 142,570" fill="var(--wave-blue)"/>
    </svg>

    <div class="brand">
      <span class="brand-dot"></span>
      <p class="brand-name">Talvane Property Services</p>
    </div>
    <p class="holder">Derek Hollingsby CEng, MSoHTF</p>

    <h2 class="services-title">Services</h2>
    <ul class="service-list">
      <li><svg class="icon" viewBox="0 0 22 22"><polyline points="3,12 9,18 20,5" fill="none" stroke="var(--deep-blue)" stroke-width="2.6"/></svg>Legionella Risk Assessment</li>
      <li><svg class="icon" viewBox="0 0 22 22"><polyline points="3,12 9,18 20,5" fill="none" stroke="var(--deep-blue)" stroke-width="2.6"/></svg>Portable Appliance Testing</li>
      <li><svg class="icon" viewBox="0 0 22 22"><polyline points="3,12 9,18 20,5" fill="none" stroke="var(--deep-blue)" stroke-width="2.6"/></svg>Energy Performance Certificate</li>
    </ul>

    <ul class="contact-list">
      <li><svg class="icon" viewBox="0 0 22 22"><rect x="6" y="2" width="11" height="18" rx="2" fill="var(--deep-blue)"/><rect x="8" y="5" width="7" height="9" fill="#fff"/></svg>07921 458 302</li>
      <li><svg class="icon" viewBox="0 0 22 22"><rect x="3" y="6" width="16" height="11" fill="var(--deep-blue)"/><polyline points="3,6 11,12 19,6" fill="none" stroke="#fff" stroke-width="1.5"/></svg>info@talvaneps-example.com</li>
      <li><svg class="icon" viewBox="0 0 22 22"><circle cx="11" cy="11" r="8.5" fill="var(--deep-blue)"/><g fill="none" stroke="#fff" stroke-width="1.2"><ellipse cx="11" cy="11" rx="3.5" ry="8.5"/><line x1="2.5" y1="11" x2="19.5" y2="11"/></g></svg>www.talvaneps-example.com</li>
      <li><svg class="icon" viewBox="0 0 22 22"><polygon points="11,2 21,11 18,11 18,20 13,20 13,14 9,14 9,20 4,20 4,11 1,11" fill="var(--deep-blue)"/></svg>Glenmorrow, Aberdeen</li>
    </ul>
  </div>
</body>
</html>
```